Vapora Nest

An e-commerce website targeting B2B and B2C customers.

High level requirements are:

Selling Tobacco Hooka Products
Home Page
English/Arabic
Main Rotating Banner
Login / Registration
Multiple delivery address
Temporary delivery address
Online payment
My account page / Order History / addresses / Payment info
Contact us page
About
Reviews 5 star rating system
Social media share buttons and email on each product page
Purchase quantity
Recommendations
Information and specifications on each product
Main search and tab bar at the top remains at the top when scrolling down
website should work seamlessly across all devise browsers adapting to the screen size mobile friendly
Whole sale page and login
Individual brand pages (i.e. Glimwave, Tova, Marno…) accessible from the first page drop down menu
Single product endless scrolling design no pages, with search, filter and sort menu at the top and how many products found
Design should be clean / clear / uncluttered / simple / easy / light / friendly and straight to the point
Currency convention automatically through I.P address

Best example i wouldn’t mind and exact copy is http://brindel.quoventaco.com

```html
<!DOCTYPE html>
<html lang="en">
<head>
<meta charset="utf-8">
<title>Vapora Nest</title>
<link href="https://fonts.googleapis.com/css2?family=Signika:wght@400;600&family=Arimo:wght@400;700&display=swap" rel="stylesheet">
<style>
:root{
  --red:#d0161a;
  --black:#000;
  --ink:#333;
  --muted:#666;
  --soft:#999;
  --rule:#e2e2e2;
  --white:#fff;
  --btn:#3a3a3a;
  --foot-text:#aaa;
}
*{margin:0;padding:0;box-sizing:border-box}
html,body{width:1076px;height:1200px;overflow:hidden;background:var(--white)}
body{position:relative;font-family:"Arimo",Arial,sans-serif;color:var(--ink)}
.abs{position:absolute}

/* header */
.brand{left:282px;top:10px;font:400 24px/30px "Signika",Arial,sans-serif;color:var(--red)}
.nav-link{top:19px;font:400 7.5px "Arimo",Arial,sans-serif;color:var(--muted);white-space:nowrap}
.search{left:671px;top:14px;width:108px;height:20px;border:1px solid #bbb;border-radius:11px}
.search svg{position:absolute;right:9px;top:4px}
.cart{left:786px;top:14px;width:20px;height:20px;border:1px solid #bbb;border-radius:50%}
.cart svg{position:absolute;left:4px;top:5px}

/* hero */
.hero{left:0;top:50px;width:1076px;height:225px;background:var(--black)}
.hero-title{left:282px;top:129px;font:400 22px/24px "Signika",Arial,sans-serif;color:var(--red)}
.hero-sub{left:282px;top:153px;font:400 13px/16px "Signika",Arial,sans-serif;color:var(--red)}
.hero-lead{left:282px;top:182px;font:400 9px "Arimo",Arial,sans-serif;color:#ddd}
.hero-btn{left:282px;top:213px;width:84px;height:23px;background:var(--btn);color:#ccc;font:400 8px/23px "Arimo",Arial,sans-serif;text-align:center;border-radius:2px;letter-spacing:.3px}
.hero-visual{left:550px;top:115px;width:260px;height:125px;border-radius:50%;background:radial-gradient(ellipse at center,#4a4a4a 0%,#222 55%,#000 75%)}

/* promo tiles */
.tile{top:290px;height:112px;color:var(--white);font:700 8px/12px "Arimo",Arial,sans-serif;letter-spacing:.6px}
.tile-gallery{left:281px;width:257px;background:linear-gradient(135deg,#2a2a2a,#6a1518 60%,#3a3a3a)}
.tile-sale{left:553px;width:253px;background:linear-gradient(135deg,#111,#2c2c2c 55%,#5a4a1c)}
.tile span{position:absolute;left:26px}

/* carousel */
.arrow{top:484px}
.product{top:438px;width:110px;text-align:center;font:400 8px "Arimo",Arial,sans-serif;color:var(--muted);white-space:nowrap}
.product .shot{width:64px;height:72px;margin:0 auto 10px;border-radius:6px}
.dots{left:534px;top:547px;display:flex;gap:3px}
.dots i{display:block;width:6px;height:6px;border:1px solid #bbb;border-radius:50%}
.dots i.on{background:#bbb}
.rule{left:281px;width:525px;height:1px;background:var(--rule)}

/* sections */
.kicker{left:281px;font:400 8px "Arimo",Arial,sans-serif;color:var(--muted);letter-spacing:.4px}
.post{top:632px;width:165px}
.post .shot{height:78px}
.post h3{margin-top:17px;font:400 10px/11px "Signika",Arial,sans-serif;color:var(--red)}
.post time{display:block;margin-top:5px;font:400 8px "Arimo",Arial,sans-serif;color:var(--muted)}
.more{display:flex;align-items:center;gap:4px;margin-top:10px;font:400 6.5px "Arimo",Arial,sans-serif;color:var(--muted);letter-spacing:.5px}

/* about */
.about-photo{left:281px;top:850px;width:242px;height:135px;background:linear-gradient(120deg,#3a2a1a,#1b2f40 60%,#244a52)}
.about-copy{left:538px;top:846px;width:270px;font:400 6.2px/9.5px "Arimo",Arial,sans-serif;color:var(--muted)}
.about-copy h2{font:400 10.5px/14px "Signika",Arial,sans-serif;color:var(--red);margin-bottom:8px;white-space:nowrap}
.about-copy ul{list-style:none;margin:5px 0 6px}
.about-copy li{display:flex;align-items:center;gap:8px;margin-bottom:6px;padding-left:3px}

/* footer */
.footer{left:0;top:1014px;width:1076px;height:186px;background:var(--black)}
.foot-h{font:400 11px "Signika",Arial,sans-serif;color:#ddd}
.foot-line{height:1px;background:#444}
.foot-list{font:400 7px/9.6px "Arimo",Arial,sans-serif;color:var(--foot-text);list-style:none;white-space:nowrap}
.blog-links{font:400 6.5px "Arimo",Arial,sans-serif;color:var(--foot-text)}
.blog-links li{list-style:none;padding:5px 0;border-bottom:1px solid #444;width:105px;white-space:nowrap}
.social{display:grid;grid-template-columns:1fr 1fr;gap:5px 6px;width:110px;font:400 7px "Arimo",Arial,sans-serif;color:var(--foot-text)}
.social span{display:flex;align-items:center;gap:4px}
.social i{display:block;width:10px;height:10px;border-radius:50%;background:#777}
.copyright{left:281px;top:1168px;font:400 6.5px "Arimo",Arial,sans-serif;color:var(--foot-text)}
.pay{top:1164px;height:22px;background:var(--white);border-radius:2px;font:700 6.5px/22px "Arimo",Arial,sans-serif;color:#333;text-align:center}
</style>
</head>
<body>

<header>
  <div class="abs brand">Vapora Nest</div>
  <nav>
    <span class="abs nav-link" style="left:454px">About Us</span>
    <span class="abs nav-link" style="left:505px">My Account</span>
    <span class="abs nav-link" style="left:558px">Ordering Info</span>
    <span class="abs nav-link" style="left:617px">Contact Us</span>
  </nav>
  <div class="abs search"><svg width="11" height="11" viewBox="0 0 11 11"><circle cx="4.5" cy="4.5" r="3.3" fill="none" stroke="#999" stroke-width="1.3"/><line x1="7" y1="7" x2="10" y2="10" stroke="#999" stroke-width="1.5"/></svg></div>
  <div class="abs cart"><svg width="11" height="9" viewBox="0 0 11 9"><path d="M0 1h2l1.5 5h5.5l1.5-4H3" fill="none" stroke="#999" stroke-width="1"/><circle cx="4" cy="8" r=".9" fill="#999"/><circle cx="8.5" cy="8" r=".9" fill="#999"/></svg></div>
</header>

<section class="abs hero"></section>
<div class="abs hero-title">Egyptian Hookah Sale</div>
<div class="abs hero-sub">Our Best Multi-Hose Hookahs</div>
<div class="abs hero-lead">Shop Hookah, Shisha Tobacco &amp; Hookah Accessories</div>
<div class="abs hero-btn">FIND OUT MORE</div>
<div class="abs hero-visual" role="img" aria-label="Multi-hose hookah with fruit pieces on a dark tray"></div>

<div class="abs tile tile-gallery" role="img" aria-label="Tobacco tins and packaging"><span style="top:82px">EXPLORE THE GALLERY</span></div>
<div class="abs tile tile-sale" role="img" aria-label="Glass and gold hookah base on dark background"><span style="top:70px">ON SALE<br>GET SPECIAL DISCOUNT &amp; EMAIL UPDATE</span></div>

<svg class="abs arrow" style="left:281px" width="8" height="14" viewBox="0 0 8 14"><path d="M7 1L1 7l6 6" fill="none" stroke="#777" stroke-width="1.2"/></svg>
<svg class="abs arrow" style="left:799px" width="8" height="14" viewBox="0 0 8 14"><path d="M1 1l6 6-6 6" fill="none" stroke="#777" stroke-width="1.2"/></svg>

<div class="abs product" style="left:307px"><div class="shot" role="img" aria-label="Hookah pipe" style="background:linear-gradient(#ddd,#8a8a8a)"></div>Featured Hookah Pipe</div>
<div class="abs product" style="left:424px"><div class="shot" role="img" aria-label="Shisha tobacco tins" style="background:linear-gradient(#2a3a6a,#111)"></div>Featured Shisha Tobacco</div>
<div class="abs product" style="left:555px"><div class="shot" role="img" aria-label="Hookah charcoal box" style="background:linear-gradient(135deg,#c0281e,#5a0e0a)"></div>Featured Hookah Charcoal</div>
<div class="abs product" style="left:673px"><div class="shot" role="img" aria-label="Red clay hookah bowl" style="background:linear-gradient(#e02a2a,#8a0c0c);border-radius:30px 30px 12px 12px"></div>Featured Hookah Accessory</div>
<div class="abs dots"><i></i><i class="on"></i><i></i></div>

<div class="abs rule" style="top:577px"></div>
<div class="abs kicker" style="top:606px">LATEST BLOG, MONTHLY GIVEAWAY &amp; DISCOUNTS</div>

<article class="abs post" style="left:281px">
  <div class="shot" role="img" aria-label="Group sharing a hookah" style="background:linear-gradient(120deg,#2a1a10,#8a5a2a 60%,#1a1a1a)"></div>
  <h3>4 New Glimwave E-Juice Flavors</h3>
  <time>25 JUN 2014</time>
  <div class="more">READ BLOG ARTICLE <svg width="6" height="5" viewBox="0 0 6 5"><path d="M0 2.5h4M3 .5l2 2-2 2" stroke="#d0161a" fill="none"/></svg></div>
</article>
<article class="abs post" style="left:461px">
  <div class="shot" role="img" aria-label="Glass hookah with red hose" style="background:linear-gradient(120deg,#6a6a5a,#b0a890 50%,#8a1a1a)"></div>
  <h3>Orvel Shroom Hookah and Orvel Prince<br>Hookah - New Glass Hookahs</h3>
  <time>25 JUN 2014</time>
  <div class="more">READ MONTHLY GIVEAWAY <svg width="6" height="5" viewBox="0 0 6 5"><path d="M0 2.5h4M3 .5l2 2-2 2" stroke="#d0161a" fill="none"/></svg></div>
</article>
<article class="abs post" style="left:641px">
  <div class="shot" role="img" aria-label="Hookah and shisha offer graphic" style="background:linear-gradient(120deg,#f2f2f2,#e8e8e8 50%,#7a2a1a)"></div>
  <h3>Shisha OFFER'S</h3>
  <time>25 JUN 2014</time>
  <div class="more">VIEW ALL OFFERS <svg width="6" height="5" viewBox="0 0 6 5"><path d="M0 2.5h4M3 .5l2 2-2 2" stroke="#d0161a" fill="none"/></svg></div>
</article>

<div class="abs rule" style="top:810px"></div>
<div class="abs kicker" style="top:828px">ABOUT VAPORA NEST</div>
<div class="abs about-photo" role="img" aria-label="Person smoking a hookah in a lounge"></div>
<div class="abs about-copy">
  <h2>Buy from the world's favorite hookah and shisha store!</h2>
  <p>We at Vaporanest.com love hookahs and hookah products, but the thing we love most about hookahs are you: our fellow hookah enthusiasts! Our goal is to keep you up and breakin' by providing:</p>
  <ul>
    <li><svg width="6" height="5" viewBox="0 0 6 5"><path d="M.5 2.5l1.7 1.7L5.5.5" stroke="#666" fill="none"/></svg>The best customer service in the hookah world</li>
    <li><svg width="6" height="5" viewBox="0 0 6 5"><path d="M.5 2.5l1.7 1.7L5.5.5" stroke="#666" fill="none"/></svg>Fastest Shipping and Packaging</li>
    <li><svg width="6" height="5" viewBox="0 0 6 5"><path d="M.5 2.5l1.7 1.7L5.5.5" stroke="#666" fill="none"/></svg>Customer-picked selection, employee backed experience</li>
  </ul>
  <p>We have a lowest price guarantee on all hookahs, shisha, hookah accessories and hookah charcoal. We will match retail competitor's website prices if your order isn't already discounted. Earn Hookah Reward Points on every order, and save them up for additional discounts!</p>
  <div class="more" style="margin-top:12px">MORE ABOUT <svg width="6" height="5" viewBox="0 0 6 5"><path d="M0 2.5h4M3 .5l2 2-2 2" stroke="#d0161a" fill="none"/></svg></div>
</div>

<footer class="abs footer"></footer>
<div class="abs foot-h" style="left:281px;top:1050px">Site Info</div>
<div class="abs foot-line" style="left:281px;top:1070px;width:202px"></div>
<ul class="abs foot-list" style="left:281px;top:1080px"><li>Shipping and Return</li><li>Right of Withdraw</li><li>Imprint</li><li>Privacy Notice</li><li>Contact Us</li></ul>
<ul class="abs foot-list" style="left:408px;top:1080px"><li>Create New Account</li><li>Login</li><li>Track your order</li><li>Shopping Cart</li></ul>

<div class="abs foot-h" style="left:529px;top:1050px">Latest Blog Post</div>
<div class="abs foot-line" style="left:529px;top:1070px;width:104px"></div>
<ul class="abs blog-links" style="left:529px;top:1084px"><li>Lorem Ipsum is simply dummy text</li><li>Lorem Ipsum is simply dummy text</li><li style="border:none">Lorem Ipsum is simply dummy text</li></ul>

<div class="abs foot-h" style="left:680px;top:1049px">Social Link</div>
<div class="abs foot-line" style="left:680px;top:1069px;width:101px"></div>
<div class="abs social" style="left:680px;top:1078px"><span><i></i>Linkbook</span><span><i></i>Chirpline</span><span><i></i>Workmesh</span><span><i></i>Callwave</span></div>

<div class="abs foot-line" style="left:281px;top:1154px;width:525px"></div>
<div class="abs copyright">Copyright © 2014 Company Name</div>
<div class="abs pay" style="left:712px;width:30px">Paynet</div>
<div class="abs pay" style="left:745px;width:29px">Cardora</div>
<div class="abs pay" style="left:777px;width:30px">Vinta</div>

</body>
</html>
```